Small Accounting Practice needs something creative

We need a business card design for a new small accounting practice based in Perth, Australia. The name of the practice is 'Kelvarin Ledger Group Pty Ltd'. We providing Tax, Bookkeeping and Accounting services. Our target are individuals and small businesses. We want the design to be simply and creative. Also, we can the design can help us to gain people's trust.

Target Market(s)

Individuals and small businesses.

Industry/Entity Type

Accounting

Colors

Designer to choose colors to be used in the design.

```html
<!DOCTYPE html>
<html lang="en">
<head>
<meta charset="utf-8">
<title>Kelvarin Ledger Group – Business Card</title>
<link href="https://fonts.googleapis.com/css2?family=Didact+Gothic&display=swap" rel="stylesheet">
<style>
  :root {
    --navy: #475a80;
    --navy-deep: #3e4f72;
    --paper: #ffffff;
    --ink: #475a80;
    --backdrop: #e9eaed;
  }
  * { margin: 0; padding: 0; box-sizing: border-box; }
  html, body { width: 1200px; height: 720px; overflow: hidden; }
  body {
    background: var(--backdrop);
    font-family: "Didact Gothic", "Century Gothic", sans-serif;
    display: flex;
    align-items: center;
    justify-content: center;
    gap: 60px;
  }
  .card {
    width: 510px;
    height: 292px;
    position: relative;
    overflow: hidden;
    box-shadow: 0 10px 28px rgba(30, 40, 60, 0.18);
  }

  /* Front */
  .card-front { background: var(--paper); color: var(--ink); }
  .front-brand {
    position: absolute; top: 30px; left: 32px;
    display: flex; align-items: center; gap: 10px;
  }
  .brand-square { width: 16px; height: 16px; background: var(--navy); }
  .brand-name { font-size: 19px; color: var(--navy); letter-spacing: 0.2px; }
  .contact-person {
    position: absolute; right: 34px; top: 128px; text-align: right;
  }
  .person-name { font-size: 30px; letter-spacing: 0.5px; margin-bottom: 6px; }
  .person-role, .person-reg { font-size: 14.5px; line-height: 1.4; }
  .contact-band {
    position: absolute; left: 0; right: 0; bottom: 0; height: 52px;
    background: var(--navy);
    color: var(--paper);
    display: flex; align-items: center;
    padding: 0 32px;
    font-size: 13.5px;
    gap: 70px;
  }
  .band-tab {
    position: absolute; right: 0; bottom: 52px;
    width: 110px; height: 22px; background: var(--navy);
  }

  /* Back */
  .card-back {
    background: var(--navy);
    color: var(--paper);
    display: flex; flex-direction: column; align-items: center; justify-content: center;
  }
  .back-brand { display: flex; align-items: center; gap: 14px; }
  .back-brand .brand-square { width: 22px; height: 22px; background: var(--paper); }
  .back-brand .brand-name { color: var(--paper); font-size: 28px; }
</style>
</head>
<body>
  <section class="card card-front" aria-label="Business card front">
    <div class="front-brand">
      <span class="brand-square"></span>
      <span class="brand-name">Kelvarin Ledger Group Pty Ltd</span>
    </div>
    <div class="contact-person">
      <p class="person-name">Tomas Reyler</p>
      <p class="person-role">Accountant &amp; Small Business Consultant</p>
      <p class="person-reg">Registered ASIC Agent 40961</p>
    </div>
    <div class="band-tab"></div>
    <div class="contact-band">
      <span class="contact-phone">Phone: 0412 555 208</span>
      <span class="contact-email">Email: tomas@kelvarinledger.com.au</span>
    </div>
  </section>

  <section class="card card-back" aria-label="Business card back">
    <div class="back-brand">
      <span class="brand-square"></span>
      <span class="brand-name">Kelvarin Ledger Group Pty Ltd</span>
    </div>
  </section>
</body>
</html>
```